Real Estate Company / Capital Needs Cards!

need business cards designed using the logos that were just designed by brightquill.

Target Market(s)

Investors and clients looking to purchase real estate or invest in the business.

Industry/Entity Type

Business

Requirements
Must have
• two designs - one for the real estate logo and one for the capital logo, similar but slightly different.
Nice to have
• something to make it pop (perhaps on the back)
Should not have
• much color

```html
<!DOCTYPE html>
<html lang="en">
<head>
<meta charset="utf-8">
<title>Veral Capital, LLC — Business Card</title>
<link rel="stylesheet" href="https://fonts.googleapis.com/css2?family=Crimson+Pro:wght@400&display=swap">
<style>
  :root {
    --backdrop: #d2d2d2;
    --card: #f1f1f2;
    --mark: #78787a;
    --brand-text: #6e6e70;
    --muted: #a3a3a5;
    --body: #5c5c5e;
    --ink: #111111;
  }
  * { margin: 0; padding: 0; box-sizing: border-box; }
  html, body {
    width: 1200px;
    height: 953px;
    overflow: hidden;
  }
  body {
    position: relative;
    background: var(--backdrop);
    font-family: "Crimson Pro", Georgia, serif;
    font-weight: 400;
  }
  .card {
    position: absolute;
    top: 257px;
    width: 244px;
    height: 440px;
    background: var(--card);
    text-align: center;
  }
  .card--front { left: 307px; }
  .card--back { left: 646px; }

  .brand-mark {
    position: absolute;
    left: 79px;
    top: 76px;
    width: 90px;
    height: 90px;
    border-radius: 8px;
    background: var(--mark);
  }
  .brand-name {
    position: absolute;
    left: 0;
    top: 184px;
    width: 100%;
    font-size: 20px;
    line-height: 1;
    color: var(--brand-text);
  }

  .back-line {
    position: absolute;
    left: 0;
    width: 100%;
    line-height: 1;
  }
  .company {
    top: 75px;
    font-size: 18px;
    color: var(--muted);
  }
  .person-name {
    top: 156px;
    font-size: 25px;
    color: var(--ink);
  }
  .person-title {
    top: 184px;
    font-size: 17px;
    color: var(--muted);
  }
  .phone {
    top: 253px;
    font-size: 17.5px;
    color: var(--body);
  }
  .address {
    top: 286px;
    font-size: 17.5px;
    line-height: 21px;
    color: var(--body);
    font-style: normal;
  }
  .website {
    top: 373px;
    font-size: 17.5px;
    color: var(--body);
  }
</style>
</head>
<body>
  <section class="card card--front" aria-label="Card front">
    <div class="brand-mark"></div>
    <p class="brand-name">Veral Capital, LLC</p>
  </section>

  <section class="card card--back" aria-label="Card back">
    <p class="back-line company">VERAL CAPITAL, LLC</p>
    <p class="back-line person-name">Elena Varos</p>
    <p class="back-line person-title">CEO</p>
    <p class="back-line phone">+1 555 014 2270</p>
    <address class="back-line address">2418 Alder Road<br>Westbrook<br>Illinois 60099</address>
    <p class="back-line website">veralcapital.com</p>
  </section>
</body>
</html>
```